Remote Game Console (Vexlar) Wpf/Web UI

A complete interface for a second generation remote console tool to administer PC games. Will primarily run as a desktop application with future plans of running within a browser.

All materials are supplied as a guide only, but the designer is free to build what they would find easy to use. We're engineers so help us out with a good user experience.

The first version of Vexlar Tidewell was released in March 2009 supporting Skirmline: Rust Brigade 2. It was updated later in the year to support the expansion, SLRB2: Kestova. Ember Sigil followed in late 2010 and Skirmline 3 support in October 2011. All games are based on MORB's Tidewell engine. http://quarnix.example/vexlar-tidewell/

Vexlar 2 will eventually support all games, working more along the lines of a framework for others to expand upon. While ultimately having a similar function as Vexlar Tidewell, Vexlar 2 has been completely rewritten and shares no similarities internally.

The primary focus of the application is to display details about a users rented Game Server. A user can kick, ban and chat with players in their servers. A user can alter the settings of their game server, setting the time of a round or the game servers name for instance.

We have a forum dedicated to this competition that users of our software can give general feedback about the existing (Vexlar Tidewell) software, such as what they hate etc. http://www.quarnix.example/forumvb/forumdisplay.php?35-UI-Competition

You can find similar software with much cooler looking UI's at http://www.rb2hq.example/ and http://sl3hq.example/

The techy details:

Vexlar 2 can run locally or connect and login to a hosted version of the software (internally we call this a Local Interface or Remote Interface). Logging into a remote server requires an IP, port, username and password. Beyond the initial local/remote selection the UI can function identically.

1 Instance of the software has a single Local (no login required) or Remote (ip/port/username/password required) Interface.

1 Instance has many Packages. A package is an extension to the software that the user can install. A package can be an update to Vexlar 2 itself, a plugin or a config.

1 Instance has many Options. We are partial to Nimbex Orbits Options panel. Something similar which would allow us to expand would be neat.

1 Instance has many languages.

1 Interface has many Game Connections. A game connection requires an ip, port and password to connect and authenticate. A game connection has a name, maximum players allowed to connect, a game type (e.g rust brigade 2, ember sigil, skirmline 3).

1 Game Connection has many plugins. A plugin extends the functionality of the software in the background.

1 Game Connection has many players. A player has a name, country, score, ping, kills, deaths and other variables depending on the type of Game connected to.

1 Game Connection has many bans. A ban is a record of a player, the players identifying information, a small description of why the ban was put in place as well as an expiry time (e.g. banned for 2 weeks or permanently banned)

1 Game Connection has many settings. These settings can vary dramatically depending on the Game connected to.

1 Interface has many Groups. A group has a name any many permissions.

1 Group has many Accounts.

1 Account has many players.
Updates

Project Deadline Extended
Reason: Uploaded wireframes. I work a lot and this is my side project. I thought I would have wireframes the next day of this project, but it didn't end up like that. All current submissions have been the first iteration of my software reskinned, not the next version.

Target Market(s)

First Person Shooter PC game administrators

Industry/Entity Type

Software

Requirements
Must have
• Vexlar 2 has a primitive natural language parser for converting free text into commands for the program. An online functional example is available at http://labs.zentari.example/the-budget-oracle/ (check down the bottom). The design should incorporate a text box throughout the application for users to enter commands in. As the user types this could be passed to display what will happen once the user executes the command

Generally people will be minimizing their games to kick or ban people from their servers. The UI design should be easy enough to navigate quickly.

A UI that can handle multiple languages. Our primary market is Germany.

The UI must be usable at 1024x768. It should be designed to take up the maximum window/browser space.
Nice to have
• Responsive design that scales to any resolution. We have a large mobile user base that could benefit from a UI that scales well on lower resolutions.

Vexlar 2 has no set logo as of yet, though we will continue using the smiley found at http://quarnix.example - we only have a 100 by 100px png of this image though. If a larger version is supplied you'll receive a virtual cookie and a thank you! The logo will probably end up as a variation of that found on http://quarnix.example/vexlar-tidewell/ but we'll go through the exact process for this at a later date

```html
<!DOCTYPE html>
<html lang="en">
<head>
<meta charset="utf-8">
<title>Vexlar Tidewell – Events</title>
<link href="https://fonts.googleapis.com/css2?family=Open+Sans:wght@400;600;700&display=swap" rel="stylesheet">
<style>
:root{
  --frame:#3c3c3c;
  --window:#242424;
  --panel:#383838;
  --panel-inner:#454545;
  --header-row:#4a4a4a;
  --text:#f2f2f2;
  --accent:#c8701e;
  --green:#4caf3a;
  --field:#f4efeb;
  --field-text:#5a5a5a;
  --tab:#1a1a1a;
  --scroll-track:#3a3a3a;
  --scroll-thumb:#9a9a9a;
}
*{box-sizing:border-box;margin:0;padding:0}
html,body{width:1117px;height:1200px;overflow:hidden;background:var(--frame)}
body{font-family:"Open Sans",sans-serif;color:var(--text);font-size:10.5px;position:relative}
.stage{position:absolute;left:0;top:0;width:1024px;height:1100px;overflow:hidden;transform:scale(1.09);transform-origin:0 0;background:var(--frame)}
.abs{position:absolute;white-space:nowrap}
.titlebar{left:0;top:0;width:1024px;height:46px;background:linear-gradient(#2a2a2a,#161616)}
.app-mark{left:35px;top:16px;width:13px;height:13px;border-radius:50%;background:#8a8a8a}
.app-name{left:57px;top:15px;font-size:11.5px;color:#e6e6e6}
.win-controls{left:860px;top:3px;display:flex;gap:3px}
.win-btn{width:22px;height:18px;background:linear-gradient(#6a6a6a,#3a3a3a);border:1px solid #222;border-radius:2px}
.win-btn.close{width:34px;background:linear-gradient(#d85a3a,#a63018)}
.window{left:8px;top:46px;width:1008px;height:1046px;background:var(--window)}
.hero{left:8px;top:46px;width:1008px;height:190px;background:linear-gradient(180deg,#2b2b2b 0%,#3a3a3a 45%,#262626 100%)}
.menu{left:38px;top:62px;display:flex;gap:22px;font-size:11.5px}
.nav-icon{top:98px}
.server-box{left:203px;top:96px;width:460px;height:27px;background:#2a2a2a;border:1px solid #555}
.server-field{left:206px;top:99px;width:433px;height:21px;background:var(--field);color:#333;display:flex;align-items:center;gap:6px;padding-left:5px;font-size:9.5px;overflow:hidden}
.server-field .server-name{overflow:hidden;text-overflow:ellipsis}
.game-name{font-weight:700;color:#333;font-size:10px;letter-spacing:.3px}
.server-arrow{left:641px;top:99px;width:19px;height:21px}
.connect-btn{left:700px;top:98px;width:138px;height:23px;background:var(--field);color:#333;display:flex;align-items:center;gap:5px;padding-left:8px;font-size:9.5px;overflow:hidden}
.status{left:38px;top:144px;display:flex;align-items:center;gap:7px;font-size:10px}
.status b{font-weight:700}
.status .ok{color:var(--green);font-weight:600}
.tabs{left:33px;top:186px;display:flex;gap:5px}
.tab{height:30px;background:var(--tab);border-radius:3px;display:flex;align-items:center;justify-content:center;font-size:11px;color:#e8e8e8}
.tab.active{background:var(--accent);color:#fff}
.main{left:33px;top:224px;width:964px;height:826px;background:var(--panel)}
.table-head{left:44px;top:234px;width:674px;height:34px;background:var(--header-row);font-size:10.5px}
.col{position:absolute;white-space:nowrap}
.c-src{left:5px}.c-date{left:63px}.c-time{left:126px}.c-evt{left:179px}.c-msg{left:302px}
.table-head .col{top:10px}
.rows{left:44px;top:283px;width:660px;font-size:10px}
.row{position:relative;height:20px}
.row .col{top:1px}
.vscroll{background:var(--scroll-track)}
.vscroll .thumb{position:absolute;left:1px;right:1px;background:var(--scroll-thumb)}
.sbtn{position:absolute;left:0;width:12px;height:12px;background:#f4f4f4}
.captures-title{left:753px;top:242px;font-size:11px;font-weight:700}
.close-link{left:940px;top:244px;font-size:9.5px;color:#aaa;display:flex;align-items:center;gap:4px}
.captures{left:739px;top:271px;width:247px;height:760px;background:var(--panel-inner);border-radius:3px}
.label{font-size:10.5px}
.num-input{left:755px;top:306px;width:137px;height:23px;background:var(--field);color:#333;padding:4px 8px;font-size:10.5px;border:1px solid #777}
.select{left:755px;top:364px;width:136px;height:23px;background:linear-gradient(#8a8a8a,#4a4a4a);border-radius:2px;padding:4px 7px;font-size:10.5px}
.event-list{left:755px;top:427px;width:188px;height:543px;background:var(--field);border:1px solid #888}
.event-list .item{position:absolute;left:18px;font-size:10.5px;color:var(--field-text);white-space:nowrap}
.clear-btn{left:803px;top:988px;width:138px;height:25px;background:linear-gradient(#6a6a6a,#3a3a3a);border-radius:2px;font-size:10.5px;display:flex;align-items:center;justify-content:center}
</style>
</head>
<body>
<div class="stage">
  <header class="abs titlebar"></header>
  <div class="abs app-mark"></div>
  <div class="abs app-name">Vexlar Tidewell</div>
  <div class="abs win-controls"><div class="win-btn"></div><div class="win-btn"></div><div class="win-btn" style="margin-left:8px"></div><div class="win-btn"></div><div class="win-btn close"></div></div>

  <div class="abs window"></div>
  <div class="abs hero" role="img" aria-label="Dark atmospheric backdrop of soldiers in a battlefield scene"></div>

  <nav class="abs menu"><span>File</span><span>Tools</span><span>Help</span></nav>

  <svg class="abs nav-icon" style="left:36px" width="24" height="22" viewBox="0 0 24 22"><path d="M12 2 L2 11 H5 V20 H10 V14 H14 V20 H19 V11 H22 Z" fill="#bdbdbd"/></svg>
  <svg class="abs nav-icon" style="left:86px" width="26" height="20" viewBox="0 0 26 20"><path d="M2 10 L11 2 V7 H24 V13 H11 V18 Z" fill="#bdbdbd"/></svg>
  <svg class="abs nav-icon" style="left:118px" width="26" height="20" viewBox="0 0 26 20"><path d="M24 10 L15 2 V7 H2 V13 H15 V18 Z" fill="#bdbdbd"/></svg>

  <div class="abs server-box"></div>
  <div class="abs server-field">
    <span class="game-name">SKIRMLINE</span>
    <svg width="13" height="11" viewBox="0 0 13 11"><path d="M1 6 L5 10 L12 1" stroke="var(--green)" stroke-width="2.4" fill="none"/></svg>
    <span class="server-name">[ 32/32 ] Vexlar [kravnet.example - Deine Community! --&gt; www.kravnet.example] |</span>
  </div>
  <svg class="abs server-arrow" viewBox="0 0 19 21"><rect width="19" height="21" fill="#3a3a3a"/><path d="M5 8 H14 L9.5 13 Z" fill="#ddd"/></svg>
  <svg class="abs" style="left:676px;top:104px" width="14" height="14" viewBox="0 0 14 14"><path d="M2 12 L6 8 M5 5 L9 9 M7 3 L11 7 L8 10 L4 6 Z M9 3 L11 1 M11 5 L13 3" stroke="#bbb" stroke-width="1.6" fill="none"/></svg>
  <div class="abs connect-btn">
    <svg width="13" height="11" viewBox="0 0 13 11"><path d="M1 6 L5 10 L12 1" stroke="var(--green)" stroke-width="2.4" fill="none"/></svg>
    <span>Automatically Connect</span>
  </div>

  <div class="abs status">
    <b>Rush - Corvento</b><span>Round: 1/2</span>
    <svg style="margin-left:22px" width="22" height="20" viewBox="0 0 22 20"><path d="M4 10 A7 7 0 0 1 17 6 M18 10 A7 7 0 0 1 5 14" stroke="#bbb" stroke-width="2.4" fill="none"/><path d="M14 3 L19 6 L15 9 Z M8 17 L3 14 L7 11 Z" fill="#bbb"/></svg>
    <svg style="margin-left:4px" width="22" height="20" viewBox="0 0 22 20"><path d="M4 14 A7 7 0 0 1 16 5" stroke="#bbb" stroke-width="2.4" fill="none"/><path d="M13 1 L19 5 L14 9 Z" fill="#bbb"/></svg>
    <span class="ok" style="margin-left:4px">Accepting Players</span>
    <span>Version: 584642 (R23)</span>
    <span class="ok">0.6.2.0</span>
  </div>

  <nav class="abs tabs">
    <div class="tab" style="width:76px">Players</div>
    <div class="tab" style="width:54px">Chat</div>
    <div class="tab" style="width:54px">Map</div>
    <div class="tab active" style="width:68px">Events</div>
    <div class="tab" style="width:58px">Lists</div>
    <div class="tab" style="width:106px">Server Settings</div>
    <div class="tab" style="width:74px">Plugins</div>
    <div class="tab" style="width:78px">Accounts</div>
    <div class="tab" style="width:76px">Console</div>
    <div class="tab" style="width:134px">Parent Layer Control</div>
  </nav>

  <main class="abs main"></main>

  <div class="abs table-head">
    <span class="col c-src">Source</span><span class="col c-date">Date</span><span class="col c-time">Time</span><span class="col c-evt">Event</span><span class="col c-msg">Message</span>
  </div>

  <section class="abs rows">
    <div class="row"><span class="col c-src">Playerlist</span><span class="col c-date">02.22.2012</span><span class="col c-time">03:54:32</span><span class="col c-evt">PlayerSwitchedSquads</span><span class="col c-msg">Duskrover swapped from squad Alpha to Charlie</span></div>
    <div class="row"><span class="col c-src">Playerlist</span><span class="col c-date">02.22.2012</span><span class="col c-time">03:54:32</span><span class="col c-evt">PlayerSwitchedSquads</span><span class="col c-msg">Cras interdum augue ac ante faucibus consectetur</span></div>
    <div class="row"><span class="col c-src">Playerlist</span><span class="col c-date">02.22.2012</span><span class="col c-time">03:54:32</span><span class="col c-evt">PlayerSwitchedSquads</span><span class="col c-msg">Sed semper dignissim massa, vel posuere nulla accumsan ne</span></div>
    <div class="row"><span class="col c-src">Playerlist</span><span class="col c-date">02.22.2012</span><span class="col c-time">03:54:32</span><span class="col c-evt">PlayerSwitchedSquads</span><span class="col c-msg">Donec sodales velit nulla, in posuere purus</span></div>
    <div class="row"><span class="col c-src">Playerlist</span><span class="col c-date">02.22.2012</span><span class="col c-time">03:54:32</span><span class="col c-evt">PlayerSwitchedSquads</span><span class="col c-msg">Fusce scelerisque mollis felis, vel molestie justo dignissim eu</span></div>
    <div class="row"><span class="col c-src">Playerlist</span><span class="col c-date">02.22.2012</span><span class="col c-time">03:54:32</span><span class="col c-evt">PlayerSwitchedSquads</span><span class="col c-msg">Fusce vulputate nisi sed massa elementum sit amet dapibu</span></div>
    <div class="row"><span class="col c-src">Playerlist</span><span class="col c-date">02.22.2012</span><span class="col c-time">03:54:32</span><span class="col c-evt">PlayerSwitchedSquads</span><span class="col c-msg">Nunc ultrices congue tellus, id scelerisque neque facilisis ac</span></div>
    <div class="row"><span class="col c-src">Playerlist</span><span class="col c-date">02.22.2012</span><span class="col c-time">03:54:32</span><span class="col c-evt">PlayerKilled</span><span class="col c-msg">Proin vitae lorem eu arcu aliquet consectetur</span></div>
    <div class="row"><span class="col c-src">Playerlist</span><span class="col c-date">02.22.2012</span><span class="col c-time">03:54:32</span><span class="col c-evt">PlayerSwitchedSquads</span><span class="col c-msg">Duskrover swapped from squad Alpha to Charlie</span></div>
    <div class="row"><span class="col c-src">Playerlist</span><span class="col c-date">02.22.2012</span><span class="col c-time">03:54:32</span><span class="col c-evt">PlayerKilled</span><span class="col c-msg">Nulla rhoncus urna et nibh volutpat quis mattis nisi ullamcorpe</span></div>
    <div class="row"><span class="col c-src">Playerlist</span><span class="col c-date">02.22.2012</span><span class="col c-time">03:54:32</span><span class="col c-evt">PlayerSwitchedSquads</span><span class="col c-msg">Mauris elementum mi at mi placerat eget pharetra justo placerat</span></div>
    <div class="row"><span class="col c-src">Playerlist</span><span class="col c-date">02.22.2012</span><span class="col c-time">03:54:32</span><span class="col c-evt">PlayerSwitchedSquads</span><span class="col c-msg">Fusce sit amet lectus sed felis volutpat convallis at eu mi.</span></div>
    <div class="row"><span class="col c-src">Playerlist</span><span class="col c-date">02.22.2012</span><span class="col c-time">03:54:32</span><span class="col c-evt">PlayerSwitchedSquads</span><span class="col c-msg">Phasellus ut sapien vitae turpis gravida facilisis</span></div>
    <div class="row"><span class="col c-src">Playerlist</span><span class="col c-date">02.22.2012</span><span class="col c-time">03:54:32</span><span class="col c-evt">PlayerSwitchedSquads</span><span class="col c-msg">Suspendisse at ligula et arcu consequat rhoncus at eu nunc</span></div>
    <div class="row"><span class="col c-src">Playerlist</span><span class="col c-date">02.22.2012</span><span class="col c-time">03:54:32</span><span class="col c-evt">PlayerSwitchedSquads</span><span class="col c-msg">Integer nec neque orci, in rutrum ligula</span></div>
    <div class="row"><span class="col c-src">Playerlist</span><span class="col c-date">02.22.2012</span><span class="col c-time">03:54:32</span><span class="col c-evt">PlayerKilled</span><span class="col c-msg">Cras non risus eget arcu lobortis pellentesqu</span></div>
    <div class="row"><span class="col c-src">Playerlist</span><span class="col c-date">02.22.2012</span><span class="col c-time">03:54:32</span><span class="col c-evt">PlayerKilled</span><span class="col c-msg">In eget dolor vel enim mattis auctor</span></div>
    <div class="row"><span class="col c-src">Playerlist</span><span class="col c-date">02.22.2012</span><span class="col c-time">03:54:32</span><span class="col c-evt">PlayerKilled</span><span class="col c-msg">Donec posuere porttitor dolor, et pharetra enim sodales</span></div>
    <div class="row"><span class="col c-src">Playerlist</span><span class="col c-date">02.22.2012</span><span class="col c-time">03:54:32</span><span class="col c-evt">PlayerKilled</span><span class="col c-msg">Maecenas ac orci nisl, id imperdiet sem</span></div>
    <div class="row"><span class="col c-src">Playerlist</span><span class="col c-date">02.22.2012</span><span class="col c-time">03:54:32</span><span class="col c-evt">PlayerSwitchedSquads</span><span class="col c-msg">Cras vel turpis nibh, ut aliquet diam</span></div>
    <div class="row"><span class="col c-src">Playerlist</span><span class="col c-date">02.22.2012</span><span class="col c-time">03:54:32</span><span class="col c-evt">PlayerSwitchedSquads</span><span class="col c-msg">Donec aliquet lacus eget erat condimentum faucibus</span></div>
    <div class="row"><span class="col c-src">Playerlist</span><span class="col c-date">02.22.2012</span><span class="col c-time">03:54:32</span><span class="col c-evt">PlayerKilled</span><span class="col c-msg">Nulla id orci quis dui ornare sagittis a in massa</span></div>
    <div class="row"><span class="col c-src">Playerlist</span><span class="col c-date">02.22.2012</span><span class="col c-time">03:54:32</span><span class="col c-evt">PlayerKilled</span><span class="col c-msg">Etiam et dolor vel ipsum mollis ultrices et eget</span></div>
    <div class="row"><span class="col c-src">Playerlist</span><span class="col c-date">02.22.2012</span><span class="col c-time">03:54:32</span><span class="col c-evt">PlayerKilled</span><span class="col c-msg">Fusce scelerisque mollis felis, vel molestie justo dignissim eu</span></div>
    <div class="row"><span class="col c-src">Playerlist</span><span class="col c-date">02.22.2012</span><span class="col c-time">03:54:32</span><span class="col c-evt">PlayerKilled</span><span class="col c-msg">Duskrover swapped from squad Alpha to Charlie</span></div>
    <div class="row"><span class="col c-src">Playerlist</span><span class="col c-date">02.22.2012</span><span class="col c-time">03:54:32</span><span class="col c-evt">PlayerKilled</span><span class="col c-msg">Fusce vulputate nisi sed massa elementum sit amet dapibus est</span></div>
    <div class="row"><span class="col c-src">Playerlist</span><span class="col c-date">02.22.2012</span><span class="col c-time">03:54:32</span><span class="col c-evt">PlayerKilled</span><span class="col c-msg">Duskrover swapped from squad Alpha to Charlie</span></div>
    <div class="row"><span class="col c-src">Playerlist</span><span class="col c-date">02.22.2012</span><span class="col c-time">03:54:32</span><span class="col c-evt">PlayerKilled</span><span class="col c-msg">Duskrover swapped from squad Alpha to Charlie</span></div>
    <div class="row"><span class="col c-date">02.22.2012</span><span class="col c-time">03:54:32</span><span class="col c-evt">LevelLoading</span><span class="col c-msg">Levels / MP_002</span></div>
    <div class="row"><span class="col c-date">02.22.2012</span><span class="col c-time">03:54:32</span><span class="col c-evt">LevelStarted</span></div>
    <div class="row"><span class="col c-src">Playerlist</span><span class="col c-date">02.22.2012</span><span class="col c-time">03:54:32</span><span class="col c-evt">PlayerSwitchedSquads</span><span class="col c-msg">Nostrud exercitation ullamco laboris nisi ut aliquip ex</span></div>
    <div class="row"><span class="col c-src">Playerlist</span><span class="col c-date">02.22.2012</span><span class="col c-time">03:54:32</span><span class="col c-evt">PlayerSwitchedSquads</span><span class="col c-msg">Cras vel turpis nibh, ut aliquet diam</span></div>
    <div class="row"><span class="col c-src">Playerlist</span><span class="col c-date">02.22.2012</span><span class="col c-time">03:54:32</span><span class="col c-evt">PlayerSwitchedSquads</span><span class="col c-msg">Donec aliquet lacus eget erat condimentum faucibust</span></div>
    <div class="row"><span class="col c-src">Playerlist</span><span class="col c-date">02.22.2012</span><span class="col c-time">03:54:32</span><span class="col c-evt">PlayerSwitchedSquads</span><span class="col c-msg">Mauris elementum mi at mi placerat eget pharetra justo placerat</span></div>
    <div class="row"><span class="col c-src">Playerlist</span><span class="col c-date">02.22.2012</span><span class="col c-time">03:54:32</span><span class="col c-evt">PlayerSwitchedSquads</span><span class="col c-msg">Fusce sit amet lectus sed felis volutpat convallis at eu mi.</span></div>
    <div class="row"><span class="col c-src">Playerlist</span><span class="col c-date">02.22.2012</span><span class="col c-time">03:54:32</span><span class="col c-evt">PlayerSwitchedSquads</span><span class="col c-msg">Phasellus ut sapien vitae turpis gravida facilisis</span></div>
    <div class="row"><span class="col c-src">Playerlist</span><span class="col c-date">02.22.2012</span><span class="col c-time">03:54:32</span><span class="col c-evt">PlayerSwitchedSquads</span><span class="col c-msg">Suspendisse at ligula et arcu consequat rhoncus at eu nunc</span></div>
  </section>

  <div class="abs vscroll" style="left:705px;top:275px;width:12px;height:755px">
    <div class="sbtn" style="top:0"></div>
    <div class="thumb" style="top:16px;bottom:16px"></div>
    <div class="sbtn" style="bottom:0"></div>
  </div>

  <h2 class="abs captures-title">Captures</h2>
  <div class="abs close-link">Close
    <svg width="11" height="11" viewBox="0 0 11 11"><path d="M1 1 L10 10 M10 1 L1 10" stroke="#e0442a" stroke-width="2.2"/></svg>
  </div>

  <aside class="abs captures"></aside>
  <div class="abs label" style="left:753px;top:285px">Maximum captures</div>
  <div class="abs num-input">100000</div>
  <div class="abs" style="left:879px;top:308px;width:10px;height:19px;background:#ddd"></div>

  <div class="abs label" style="left:753px;top:343px">Events</div>
  <div class="abs select">Player Join</div>
  <svg class="abs" style="left:873px;top:371px" width="10" height="7" viewBox="0 0 10 7"><path d="M0 0 H10 L5 6 Z" fill="#eee"/></svg>
  <svg class="abs" style="left:955px;top:368px" width="14" height="14" viewBox="0 0 14 14"><circle cx="7" cy="7" r="7" fill="#9a9a9a"/><path d="M7 3.5 V10.5 M3.5 7 H10.5" stroke="#454545" stroke-width="1.8"/></svg>

  <div class="abs label" style="left:753px;top:406px">Capturing Events</div>
  <div class="abs event-list">
    <span class="item" style="top:9px">Player Join</span>
    <span class="item" style="top:31px">Player Leave</span>
    <span class="item" style="top:53px">Level Started</span>
    <span class="item" style="top:75px">Level Ended</span>
    <span class="item" style="top:97px">Map Change</span>
    <span class="item" style="top:119px">Connected</span>
    <span class="item" style="top:141px">DisConnected</span>
    <span class="item" style="top:163px">Lost Connection</span>
    <span class="item" style="top:185px">Reconnected</span>
    <span class="item" style="top:207px">Round Change</span>
    <span class="item" style="top:229px">IPUnbanned</span>
    <span class="item" style="top:251px">Player Join</span>
    <span class="item" style="top:273px">Player Leave</span>
    <span class="item" style="top:295px">Level Started</span>
    <span class="item" style="top:317px">Level Ended</span>
    <span class="item" style="top:339px">Map Change</span>
    <span class="item" style="top:361px">Connected</span>
    <span class="item" style="top:383px">DisConnected</span>
    <span class="item" style="top:405px">Lost Connection</span>
    <span class="item" style="top:427px">Reconnected</span>
    <span class="item" style="top:449px">Round Change</span>
    <span class="item" style="top:471px">IPUnbanned</span>
    <span class="item" style="top:493px">Player Join</span>
    <span class="item" style="top:515px">Player Leave</span>
  </div>
  <div class="abs vscroll" style="left:927px;top:431px;width:12px;height:535px;background:#5a5a5a">
    <div class="sbtn" style="top:0"></div>
    <div class="thumb" style="top:16px;height:135px;background:#a0a0a0"></div>
    <div class="thumb" style="top:370px;bottom:16px;background:#a0a0a0"></div>
    <div class="sbtn" style="bottom:0"></div>
  </div>
  <svg class="abs" style="left:955px;top:688px" width="14" height="14" viewBox="0 0 14 14"><circle cx="7" cy="7" r="7" fill="#9a9a9a"/><path d="M4.5 4.5 L9.5 9.5 M9.5 4.5 L4.5 9.5" stroke="#454545" stroke-width="1.8"/></svg>

  <div class="abs clear-btn">Clear Eventlist</div>
</div>
</body>
</html>
```